KJ Automation - Stationery and Identity.

Corporate Identity Design for the company, which includes Power Point presentations, Letterheads, business cards and mail signatures. We look for a simple design, but modern and elegant, that goes hand in hand with the technology that is the engine of the company.

Target Market(s)

Industrial Sector of Automation, Robotics and Process Control.

Industry/Entity Type

Automation

Colors

Designer to choose colors to be used in the design.

Requirements
Must have
• It must have an elegant, simple and clean design.

```html
<!DOCTYPE html>
<html lang="es">
<head>
<meta charset="utf-8">
<title>KJ Automation – Business Card</title>
<link href="https://fonts.googleapis.com/css2?family=Exo+2:wght@700&family=Questrial&display=swap" rel="stylesheet">
<style>
  :root {
    --page-bg: #e4e4e4;
    --card-white: #ffffff;
    --brand-blue: #1a6cb0;
    --brand-blue-light: #22a3dc;
    --brand-gray: #9a9a9a;
    --text-gray: #555555;
    --band-gray: #a3a3a3;
  }
  html, body {
    margin: 0;
    width: 1125px;
    height: 1200px;
    overflow: hidden;
    background: var(--page-bg);
  }
  .canvas {
    position: relative;
    width: 1125px;
    height: 1200px;
  }
  .card {
    position: absolute;
    left: 150px;
    width: 826px;
    height: 472px;
    box-shadow: 0 2px 6px rgba(0,0,0,0.25);
    overflow: hidden;
  }
  .card--front { top: 106px; background: var(--card-white); }
  .card--back  { top: 640px; }

  .brand-name {
    position: absolute;
    left: 40px;
    top: 200px;
    width: 360px;
    display: flex;
    align-items: center;
    justify-content: center;
    gap: 12px;
    font-family: "Questrial", sans-serif;
    font-size: 30px;
    color: var(--brand-blue);
    white-space: nowrap;
  }
  .brand-name__mark {
    width: 16px;
    height: 16px;
    background: var(--brand-blue);
  }

  .divider { position: absolute; left: 427px; width: 3px; }
  .divider--accent { top: 103px; height: 54px; background: var(--brand-blue); }
  .divider--rule { top: 162px; height: 177px; background: var(--band-gray); }

  .contact { position: absolute; left: 461px; top: 94px; }
  .contact__name {
    margin: 0;
    font-family: "Exo 2", sans-serif;
    font-weight: 700;
    font-size: 34px;
    line-height: 40px;
    color: var(--brand-blue);
  }
  .contact__title {
    margin: 0;
    font-family: "Questrial", sans-serif;
    font-size: 19px;
    color: var(--brand-gray);
  }
  .contact__address, .contact__lines {
    margin: 0;
    font-family: "Questrial", sans-serif;
    font-size: 18px;
    line-height: 25px;
    color: var(--text-gray);
  }
  .contact__address { margin-top: 20px; }
  .contact__lines { margin-top: 14px; line-height: 26px; }
  .contact__label { color: var(--brand-blue); font-weight: 700; }
  .contact__email { font-size: 15px; }

  .footer-band { position: absolute; left: 0; bottom: 0; width: 826px; height: 50px; }
  .website {
    position: absolute;
    left: 84px;
    bottom: 16px;
    font-family: "Questrial", sans-serif;
    font-size: 16px;
    color: #ffffff;
    letter-spacing: 0.3px;
  }

  .back-pattern {
    position: absolute;
    inset: 0;
    background: radial-gradient(ellipse at 55% 60%, #2aa5df 0%, #1d86c8 45%, #1667ab 100%);
  }
  .back-name {
    position: absolute;
    left: 0;
    top: 214px;
    width: 826px;
    text-align: center;
    font-family: "Questrial", sans-serif;
    font-size: 40px;
    color: #ffffff;
  }
</style>
</head>
<body>
<main class="canvas">

  <section class="card card--front">
    <div class="brand-name"><span class="brand-name__mark"></span>KJ Automation</div>

    <div class="divider divider--accent"></div>
    <div class="divider divider--rule"></div>

    <div class="contact">
      <h1 class="contact__name">MARCO REYES</h1>
      <p class="contact__title">CEO/FOUNDER</p>
      <p class="contact__address">
        Calle Robles No. 418<br>
        Col. Jardines del Valle C.P. 45010<br>
        Zapotlán, Jalisco, Mexico
      </p>
      <p class="contact__lines">
        <span class="contact__label">P:</span> (+52) 33-4810-2267<br>
        <span class="contact__label">C:</span> 33-5902-4481<br>
        <span class="contact__email">mreyes@kjautomation.com.mx</span>
      </p>
    </div>

    <svg class="footer-band" viewBox="0 0 826 50" aria-hidden="true">
      <defs>
        <linearGradient id="bandBlue" x1="0" x2="1" y1="0" y2="0">
          <stop offset="0" stop-color="#1667ab"/>
          <stop offset="1" stop-color="#22a3dc"/>
        </linearGradient>
      </defs>
      <polygon points="0,1 396,1 434,50 0,50" fill="url(#bandBlue)"/>
      <polygon points="410,18 826,18 826,33 422,33" fill="#a3a3a3"/>
      <line x1="426" y1="26" x2="810" y2="26" stroke="#ffffff" stroke-width="2"/>
      <circle cx="816" cy="26" r="6" fill="#a3a3a3" stroke="#ffffff" stroke-width="2"/>
    </svg>
    <div class="website">www.kjautomation.com.mx</div>
  </section>

  <section class="card card--back">
    <div class="back-pattern" role="img" aria-label="Blue background with a faint repeating brand pattern"></div>
    <div class="back-name">KJ Automation</div>
  </section>

</main>
</body>
</html>
```